GLIM TOD BY FERN LOOP CO

We plan to use a rum product from the caribbean country of Belize CA. That will need to be mentioned somewhere on the label. We want to do a more high-line product, an aged dark rum that plays on the shark theme. We want to use a sleek bottle design with a clever label. Or unique label placement. We need something that will pop off the shelf. We want you to have fun with it and see where it goes. We like the idea of sharks circling around the bottle, possibly like an etching on the glass or back printed on the label or a clear label that can feature the sharks in some capacity. (Not a must) "Chum" because it attracts sharks.

The "Glim Tod" needs a FONT that can become synonymous with the word and then the product. Glim Tod is to be the focus and Fern Loop Co is merely the parent company and requires mention.
Ex:
Fern Loop co.'s Glim Tod
produced in Belize, CA
or Glim Tod produced in Belize for
Fern Loop co.

We have a Glim Tod "mascot" or stamp that is a tribal shark drawing that we want used in the designs where ever you feel fit. We like the stamp as it is, but if you have some tweaks we may consider them.
Updates

I have increased first place to $450.00  and 2nd place to$150.00 !!!

 Everything we have gotten has been great just looking for more ideas. Looking for something sharp and sleek for our bottle we are trying to sell a  upscale rum !! We need it for a aged rum & a white rum .. 

  Thank you !! 
  Orwin

Target Market(s)

MALE 25 TO 45

Industry/Entity Type

It Company

Requirements
Must have
• SHARK THEME ...
Should not have
• OLD WORLD LOOK / MAP LOOKING / TRADITIONAL/ CHEAP.
We don't want everything that has already been done, like all the pirate themes. You can hint at any of these elements in a clever understated way. It is rum after all!

```html
<!DOCTYPE html>
<html lang="en">
<head>
<meta charset="utf-8">
<title>Glim Tod – Premium Crafted Rum Label</title>
<link href="https://fonts.googleapis.com/css2?family=Open+Sans:wght@400;600&display=swap" rel="stylesheet">
<style>
  :root {
    --backdrop: #f4f4f4;
    --glass: #f1f3f3;
    --glass-edge: #cfd4d4;
    --sleeve: #1c1c1c;
    --cap: #a9d2de;
    --band: #d6262b;
    --ink: #111111;
    --paper: #ffffff;
    --shark-tone: #d2d2d2;
  }
  html, body {
    margin: 0;
    padding: 0;
    width: 1200px;
    height: 1000px;
    overflow: hidden;
    background: var(--backdrop);
  }
  .canvas { display: block; width: 1200px; height: 1000px; }
  .glass { fill: var(--glass); stroke: var(--glass-edge); stroke-width: 2; }
  .cap { fill: var(--cap); }
  .neck-band { fill: var(--band); }
  .neck-band-text {
    font-family: "Open Sans", sans-serif;
    font-size: 12px;
    font-weight: 600;
    letter-spacing: 0.5px;
    fill: var(--paper);
  }
  .sleeve { fill: var(--sleeve); }
  .mark-square { fill: var(--ink); }
  .mark-square--light { fill: var(--paper); }
  .brand-name {
    font-family: "Open Sans", sans-serif;
    font-size: 27px;
    font-weight: 600;
    fill: var(--ink);
  }
  .shark-art { fill: var(--shark-tone); }
  .tagline {
    font-family: "Open Sans", sans-serif;
    font-size: 15px;
    font-weight: 400;
    fill: var(--ink);
  }
  .producer {
    font-family: "Open Sans", sans-serif;
    font-size: 9px;
    fill: var(--ink);
  }
  .spec-bar { fill: var(--ink); }
  .spec-text {
    font-family: "Open Sans", sans-serif;
    font-size: 8.5px;
    font-weight: 600;
    fill: var(--paper);
  }
</style>
</head>
<body>
<svg class="canvas" viewBox="0 0 1200 1000" xmlns="http://www.w3.org/2000/svg">
  <!-- bottle glass -->
  <path class="glass" d="M554 200 L646 200 L646 295 Q648 330 690 338 Q718 345 718 380 L718 870 Q718 895 693 895 L507 895 Q482 895 482 870 L482 380 Q482 345 510 338 Q552 330 554 295 Z"/>

  <!-- black shoulder sleeve -->
  <path class="sleeve" d="M554 208 L646 208 L646 295 Q648 330 690 338 Q718 345 718 380 L718 420 Q672 420 664 480 Q655 552 600 555 Q545 552 536 480 Q528 420 482 420 L482 380 Q482 345 510 338 Q552 330 554 295 Z"/>
  <rect class="mark-square--light" x="594" y="262" width="12" height="12"/>

  <!-- cap and neck band -->
  <rect class="cap" x="550" y="98" width="100" height="112" rx="6"/>
  <rect class="neck-band" x="587" y="116" width="26" height="112"/>
  <text class="neck-band-text" transform="translate(605 124) rotate(90)">GLIM TOD</text>

  <!-- brand block -->
  <rect class="mark-square" x="588" y="585" width="24" height="24"/>
  <text class="brand-name" x="514" y="644" textLength="172" lengthAdjust="spacing">GLIM TOD</text>

  <rect class="shark-art" x="532" y="656" width="136" height="100" rx="40" role="img" aria-label="Faint grey tribal shark mascot illustration swimming toward the viewer"/>

  <text class="tagline" x="528" y="784" textLength="144" lengthAdjust="spacing">Premium</text>
  <text class="tagline" x="528" y="800" textLength="144" lengthAdjust="spacing">Crafted Rum</text>
  <text class="tagline" x="528" y="816" textLength="144" lengthAdjust="spacing">from Belize</text>

  <text class="producer" x="528" y="832" textLength="144" lengthAdjust="spacing">Fern Loop Co`s Glim Tod</text>
  <text class="producer" x="528" y="843" textLength="144" lengthAdjust="spacing">produced in Belize, CA</text>

  <rect class="spec-bar" x="528" y="849" width="146" height="13"/>
  <text class="spec-text" x="532" y="859">40% Alcohol.</text>
  <text class="spec-text" x="670" y="859" text-anchor="end">750 ml.</text>
</svg>
</body>
</html>
```